Design some Business Cards

Dario & Linda Kowalczyk Real Estate Investors Email DKowalczyk@harborlantern.com Phone R: (555)214-3098 S: (555)871-4425

```html
<!DOCTYPE html>
<html lang="en">
<head>
<meta charset="utf-8">
<title>Dario &amp; Linda Kowalczyk – Business Cards</title>
<link href="https://fonts.googleapis.com/css2?family=Cinzel:wght@600&family=Quicksand:wght@500;600;700&display=swap" rel="stylesheet">
<style>
  :root {
    --green: #2e8b3e;
    --paper: #ffffff;
    --backdrop: #e6e8e6;
    --on-green: #ffffff;
    --divider: rgba(255,255,255,.75);
  }
  * { margin: 0; padding: 0; box-sizing: border-box; }
  html, body { width: 1200px; height: 900px; overflow: hidden; }
  body {
    background: var(--backdrop);
    font-family: "Quicksand", sans-serif;
    position: relative;
  }
  .card {
    position: absolute;
    left: 290px;
    width: 620px;
    height: 354px;
    background: var(--paper);
    box-shadow: 0 10px 28px rgba(0,0,0,.16);
    overflow: hidden;
  }
  .card--front { top: 50px; }
  .card--back { top: 470px; }

  .brand {
    display: flex;
    align-items: center;
    gap: 12px;
    font-family: "Cinzel", serif;
    font-weight: 600;
    color: var(--green);
    letter-spacing: .5px;
    white-space: nowrap;
  }
  .brand__square {
    width: 26px; height: 26px;
    background: var(--green);
    flex: none;
  }
  .card--front .brand {
    position: absolute;
    left: 0; right: 0; top: 158px;
    justify-content: center;
    font-size: 24px;
  }
  .card--back .brand {
    position: absolute;
    left: 44px; top: 118px;
    font-size: 23px;
  }
  .card--back .brand__square { width: 30px; height: 30px; }

  .band {
    position: absolute;
    background: var(--green);
  }
  .band--side { left: 330px; right: 0; top: 172px; bottom: 0; }
  .band--base { left: 0; right: 0; bottom: 0; height: 84px; }

  .tagline {
    position: absolute;
    left: 44px; bottom: 28px;
    color: var(--on-green);
    font-size: 22px;
    font-weight: 600;
    white-space: nowrap;
  }
  .divider {
    position: absolute;
    left: 344px; top: 192px;
    width: 1.5px; height: 132px;
    background: var(--divider);
  }
  .contacts {
    position: absolute;
    left: 362px; top: 200px;
    list-style: none;
    font-size: 13px;
    font-weight: 600;
    color: var(--on-green);
    white-space: nowrap;
  }
  .contacts li {
    display: flex;
    align-items: center;
    gap: 8px;
    height: 25px;
  }
  .contacts svg { width: 14px; height: 14px; flex: none; }
</style>
</head>
<body>

<section class="card card--front" aria-label="Card front">
  <div class="brand">
    <span class="brand__square"></span>
    <span class="brand__name">Dario &amp; Linda Kowalczyk</span>
  </div>
</section>

<section class="card card--back" aria-label="Card back">
  <div class="band band--side"></div>
  <div class="band band--base"></div>

  <div class="brand">
    <span class="brand__square"></span>
    <span class="brand__name">Dario &amp; Linda Kowalczyk</span>
  </div>

  <div class="divider"></div>
  <ul class="contacts">
    <li>
      <svg viewBox="0 0 16 16" aria-hidden="true"><circle cx="8" cy="8" r="7" fill="none" stroke="#ffffff" stroke-width="1.3"/><path d="M5.2 4.3l1.3 1.5-.7 1c.5 1.1 1.3 1.9 2.4 2.4l1-.7 1.5 1.3-.8 1.1C7.6 10.6 5.4 8.4 4.1 5.1z" fill="#ffffff"/></svg>
      <span>Dario: (555)214-3098</span>
    </li>
    <li>
      <svg viewBox="0 0 16 16" aria-hidden="true"><circle cx="8" cy="8" r="7" fill="none" stroke="#ffffff" stroke-width="1.3"/><path d="M5.2 4.3l1.3 1.5-.7 1c.5 1.1 1.3 1.9 2.4 2.4l1-.7 1.5 1.3-.8 1.1C7.6 10.6 5.4 8.4 4.1 5.1z" fill="#ffffff"/></svg>
      <span>Linda: (555)871-4425</span>
    </li>
    <li>
      <svg viewBox="0 0 16 16" aria-hidden="true"><rect x="1.5" y="3.5" width="13" height="9" fill="none" stroke="#ffffff" stroke-width="1.3"/><path d="M1.5 3.5L8 9l6.5-5.5" fill="none" stroke="#ffffff" stroke-width="1.3"/></svg>
      <span>DKowalczyk@harborlantern.com</span>
    </li>
  </ul>

  <p class="tagline">Real Estate Investors</p>
</section>

</body>
</html>
```